Tilda Tinkerwire, An IT Company Has New Logo, Need Fresh Business Cards

IT company is called Tilda Tinkerwire and is displayed nicely with the new logo from here on pitchloft. Would like a fresh business card look that encompasses the idea that we want clients to Cherish Every Gadget. I love the use of circuitry with hearts as endpoints and x's and o's. It needs to have room for my certification logos of which there are 4 and a BRJ Alumni log. I am attaching my current card to illustrate how it has always captured attention, but that was in the early stages of business when I was doing more residential work. I am focused on businesses now, so a level of professionalism is necessary. I would also like the card to lend itself well to additional stationary, email signature, ticketing template for my workboard, etc. For the time being, I need the card for an upcoming conference so that work will come later. Color scheme should be that of the new logo. Thank you and I look forward to the designs.

Target Market(s)

Businesses looking for IT services.

Industry/Entity Type

Information Technology

Contact Information for Business Card

See above

Requirements
Must have
• New logo colors and a warm feel. Possibly a tad feminine as I am female, but appealing to males.
Nice to have
• I would like techy, but no too much so. I like friendly and connecting feels. People LOVED my old card and called me because it gave them a warm feeling.

```html
<!DOCTYPE html>
<html lang="en">
<head>
<meta charset="utf-8">
<title>Tilda Tinkerwire – Business Card</title>
<link rel="stylesheet" href="https://fonts.googleapis.com/css2?family=Raleway:wght@500&family=Open+Sans:wght@400;600&family=Roboto+Condensed:wght@700&display=swap">
<style>
  :root {
    --page-bg: #2b2b2b;
    --sky: #86cbe9;
    --lime: #cde083;
    --paper: #ffffff;
    --ink: #454545;
    --ink-soft: #555555;
    --badge-dark: #3a3a3a;
    --badge-blue: #5aa9da;
    --badge-gold: #b59a5c;
    --dot: #86cbe9;
  }
  html, body {
    margin: 0;
    width: 1200px;
    height: 960px;
    overflow: hidden;
    background: var(--page-bg);
  }
  .business-card {
    position: absolute;
    left: 150px;
    top: 222px;
    width: 900px;
    height: 515px;
    border-radius: 27px;
    overflow: hidden;
    background: var(--paper);
    display: flex;
    flex-direction: column;
  }
  .card-header {
    height: 136px;
    background: var(--sky);
    display: flex;
    flex-direction: column;
    align-items: center;
    justify-content: center;
    color: var(--paper);
  }
  .brand-name {
    font-family: "Raleway", sans-serif;
    font-weight: 500;
    font-size: 54px;
    line-height: 1;
    letter-spacing: -0.5px;
    margin: 6px 0 4px;
  }
  .brand-tagline {
    font-family: "Open Sans", sans-serif;
    font-weight: 600;
    font-size: 16px;
    letter-spacing: 5px;
    text-transform: uppercase;
  }
  .card-body {
    position: relative;
    height: 257px;
  }
  .contact {
    position: absolute;
    left: 51px;
    top: 50px;
    font-family: "Open Sans", sans-serif;
    color: var(--ink);
  }
  .contact-call {
    font-weight: 600;
    font-size: 27px;
    margin: 0 0 14px;
  }
  .contact-line {
    font-size: 24px;
    margin: 0;
    line-height: 34px;
    color: var(--ink-soft);
  }
  .services {
    margin: 20px 0 0;
    font-family: "Roboto Condensed", sans-serif;
    font-weight: 700;
    font-size: 27px;
    color: var(--ink);
    display: flex;
    align-items: center;
    gap: 6px;
  }
  .services .sep {
    width: 9px;
    height: 9px;
    border-radius: 50%;
    background: var(--dot);
  }
  .logo-mark-area {
    position: absolute;
    left: 615px;
    top: 30px;
    width: 225px;
    height: 200px;
    border-radius: 50%;
    background: radial-gradient(circle at 50% 45%, #e9f5fb 0%, #f4eaf4 55%, #f1f6e2 100%);
  }
  .card-footer {
    flex: 1;
    background: var(--lime);
    display: flex;
    align-items: center;
    justify-content: space-around;
    padding: 0 30px;
  }
  .badge {
    height: 52px;
    border-radius: 4px;
  }
  .badge--cert { width: 120px; background: var(--badge-dark); opacity: 0.8; }
  .badge--cert-alt { width: 100px; background: var(--badge-blue); opacity: 0.8; }
  .badge--alumni { width: 96px; background: var(--badge-gold); opacity: 0.75; }
  .badge--alumni-dark { width: 80px; background: var(--badge-dark); opacity: 0.7; }
  .badge--tech { width: 150px; height: 40px; background: var(--badge-blue); opacity: 0.7; }
</style>
</head>
<body>
  <section class="business-card">
    <header class="card-header">
      <div class="brand-name">TildaTinkerwire</div>
      <div class="brand-tagline">× o Cherish Every Gadget o ×</div>
    </header>

    <div class="card-body">
      <div class="contact">
        <p class="contact-call">Call Tilda!&nbsp; 407-555-0148</p>
        <p class="contact-line">www.tilda-tinkerwire.com</p>
        <p class="contact-line">tilda.tinkerwire@mailnest.com</p>
        <p class="services">Desktops<span class="sep"></span>Laptops<span class="sep"></span>Tablets</p>
      </div>
      <div class="logo-mark-area" role="img" aria-label="Tilda Tinkerwire heart logo mark in pastel blue, pink and green"></div>
    </div>

    <footer class="card-footer">
      <div class="badge badge--cert" role="img" aria-label="Certification badge"></div>
      <div class="badge badge--alumni" role="img" aria-label="BRJ Alumni badge"></div>
      <div class="badge badge--tech" role="img" aria-label="Technician certification badge"></div>
      <div class="badge badge--cert-alt" role="img" aria-label="Certification badge"></div>
      <div class="badge badge--cert" role="img" aria-label="Certification badge"></div>
      <div class="badge badge--alumni-dark" role="img" aria-label="BRJ Alumni club badge"></div>
    </footer>
  </section>
</body>
</html>
```